Men's enhance supplement package design (square form)

WHAT WE WANT TO TELL BY DESIGN:Male enhancement, enhance Sexual vitality, strong man, get (back) desire forsex, masculinity, booster.This supplement is not like Tolmaxe but want to tell like Tolmaxe by design.

Target Market(s)

Men who over 30 years old and feel lack of sexual desire.

```html
<!DOCTYPE html>
<html lang="en">
<head>
<meta charset="utf-8">
<title>L-Varonex – Dietary Supplement Pouch Front</title>
<link href="https://fonts.googleapis.com/css2?family=Exo+2:ital,wght@1,700;1,800&family=Russo+One&display=swap" rel="stylesheet">
<style>
  :root {
    --page: #ffffff;
    --ink: #050505;
    --red: #d8141c;
    --red-dark: #8e0a10;
    --red-bright: #f0262c;
    --silver: #c9c9c9;
    --silver-dark: #6d6d6d;
    --white: #ffffff;
    --photo-light: #8a8a8a;
    --photo-dark: #1a1a1a;
  }
  * { box-sizing: border-box; margin: 0; padding: 0; }
  html, body { width: 1200px; height: 842px; overflow: hidden; background: var(--page); }

  .pouch-front {
    position: absolute;
    left: 320px; top: 24px;
    width: 560px; height: 794px;
    background: var(--ink);
    overflow: hidden;
  }

  .hero-photo {
    position: absolute;
    left: 0; top: 232px;
    width: 400px; height: 562px;
    background:
      radial-gradient(ellipse 55% 40% at 45% 35%, var(--photo-light), transparent 70%),
      linear-gradient(180deg, #2a2a2a 0%, #5a5a5a 40%, var(--photo-dark) 100%);
  }

  .tagline {
    position: absolute;
    top: 168px; left: 0; width: 100%;
    text-align: center;
    font-family: "Exo 2", sans-serif;
    font-style: italic; font-weight: 700;
    font-size: 17px; letter-spacing: 4px;
    color: var(--red-bright);
  }

  .brand-name {
    position: absolute;
    top: 196px; left: 0; width: 100%;
    text-align: center;
    font-family: "Russo One", sans-serif;
    font-size: 50px; line-height: 1;
    color: var(--white);
  }

  .claim {
    position: absolute;
    right: 0;
    display: flex; align-items: center; justify-content: flex-end;
    padding-right: 72px;
    text-align: right;
    font-family: "Exo 2", sans-serif;
    font-style: italic; font-weight: 800;
    font-size: 19px; line-height: 1.25;
    color: var(--white);
    background: linear-gradient(90deg, var(--red-dark) 0%, var(--red) 40%, var(--red) 100%);
    border-bottom: 5px solid var(--silver);
  }
  .claim--enhancement { top: 297px; left: 192px; height: 40px; }
  .claim--vitality    { top: 345px; left: 250px; height: 70px; }
  .claim--strong      { top: 421px; left: 288px; height: 40px; }
  .claim--desire      { top: 467px; left: 300px; height: 68px; }
  .claim--booster     { top: 541px; left: 310px; height: 66px; }

  .base-shape { position: absolute; left: 0; bottom: 0; }

  .count-badge {
    position: absolute;
    left: 338px; top: 658px;
    width: 222px; height: 76px;
  }
  .count-badge__text {
    position: absolute;
    left: 30px; top: 4px; width: 140px;
    text-align: center;
    font-family: "Exo 2", sans-serif;
    font-style: italic; font-weight: 800;
    color: var(--white);
  }
  .count-badge__number { display: block; font-size: 44px; line-height: 1; }
  .count-badge__unit { display: block; font-size: 19px; line-height: 1.1; }
</style>
</head>
<body>
  <main class="pouch-front">
    <div class="hero-photo" role="img" aria-label="Black-and-white photo of a muscular shirtless man with a raised clenched fist"></div>

    <svg class="base-shape" width="560" height="120" viewBox="0 0 560 120" aria-hidden="true">
      <polygon points="185,60 560,60 560,120 180,120" fill="var(--red-dark)"/>
      <polygon points="330,80 560,60 560,120 300,120" fill="var(--red)"/>
      <polygon points="430,120 500,70 560,70 560,120" fill="var(--red-bright)"/>
    </svg>

    <p class="tagline">DIETARY SUPPLEMENT FOR MEN</p>
    <h1 class="brand-name">L-VARONEX</h1>

    <p class="claim claim--enhancement">MALE ENHANCEMENT</p>
    <p class="claim claim--vitality">ENHANCE<br>SEXUAL VITALITY</p>
    <p class="claim claim--strong">STRONG MAN</p>
    <p class="claim claim--desire">GET BACK<br>DESIRE FOR SEX</p>
    <p class="claim claim--booster">MASCULINITY<br>BOOSTER</p>

    <div class="count-badge">
      <svg width="222" height="76" viewBox="0 0 222 76" aria-hidden="true">
        <polygon points="58,2 220,2 220,74 4,74" fill="var(--ink)" stroke="var(--silver)" stroke-width="3"/>
      </svg>
      <p class="count-badge__text">
        <span class="count-badge__number">90</span>
        <span class="count-badge__unit">TABLETS</span>
      </p>
    </div>
  </main>
</body>
</html>
```